Toreva Cyber Security Capablties Brief

Design a 3 page that can stand alone or use one or two of the pages

This is capabilities brief for a company that does cyber and information security

Target Market(s)

Small to Large Companies

Industry/Entity Type

Cyber Security and Information Security

Font styles to use
Script

Requirements
Must have
• High tech look and feel, must staying in the Toreva Branding colors, expect for grapics

```html
<!DOCTYPE html>
<html lang="en">
<head>
<meta charset="UTF-8">
<title>Toreva Cyber Security – Capabilities Statement</title>
<link href="https://fonts.googleapis.com/css2?family=Poppins:wght@400;500;600;700;800&display=swap" rel="stylesheet">
<style>
  :root {
    --navy-deep: #0a1446;
    --navy: #0d2470;
    --brand-blue: #1f6fd1;
    --sky: #3fa3f0;
    --sky-soft: #6cc0ff;
    --ink: #1c2540;
    --paper: #ffffff;
    --mist: #eceef2;
  }
  * { margin: 0; padding: 0; box-sizing: border-box; }
  html, body { width: 1200px; height: 801px; overflow: hidden; }
  body {
    background: var(--paper);
    font-family: "Poppins", sans-serif;
    position: relative;
  }
  .cover { position: absolute; inset: 0; width: 1200px; height: 801px; }
  .cover-art { position: absolute; inset: 0; }

  .brand {
    position: absolute;
    left: 70px;
    top: 120px;
    display: flex;
    flex-direction: column;
    gap: 2px;
  }
  .brand-row { display: flex; align-items: center; gap: 12px; }
  .brand-mark {
    width: 18px; height: 18px;
    border-radius: 50%;
    background: var(--brand-blue);
  }
  .brand-name {
    font-weight: 700;
    font-size: 46px;
    letter-spacing: 2px;
    color: var(--brand-blue);
    line-height: 1;
  }
  .brand-tagline {
    font-weight: 500;
    font-size: 19px;
    color: var(--brand-blue);
    padding-left: 30px;
    letter-spacing: 0.5px;
  }

  .headline {
    position: absolute;
    left: 80px;
    top: 330px;
    color: var(--paper);
  }
  .headline h1 {
    font-weight: 700;
    font-size: 38px;
    line-height: 1.28;
    letter-spacing: 2px;
    text-transform: uppercase;
  }
  .headline .intro {
    margin-top: 22px;
    padding-left: 16px;
    border-left: 4px solid var(--sky);
    font-size: 17px;
    font-weight: 500;
    line-height: 1.45;
    color: var(--paper);
  }
  .headline .intro .accent { color: var(--sky); }

  .website {
    position: absolute;
    right: 70px;
    top: 668px;
    font-size: 17px;
    font-weight: 500;
    letter-spacing: 2.5px;
    color: var(--ink);
  }
</style>
</head>
<body>
<main class="cover">
  <svg class="cover-art" width="1200" height="801" viewBox="0 0 1200 801">
    <defs>
      <radialGradient id="haze" cx="1" cy="0" r="0.9">
        <stop offset="0" stop-color="#d9dde4"/>
        <stop offset="1" stop-color="#ffffff" stop-opacity="0"/>
      </radialGradient>
      <linearGradient id="bandFill" x1="0" y1="1" x2="1" y2="0">
        <stop offset="0" stop-color="var(--navy-deep)"/>
        <stop offset="0.55" stop-color="var(--navy)"/>
        <stop offset="1" stop-color="#1456b8"/>
      </linearGradient>
      <radialGradient id="shieldGlow" cx="0.5" cy="0.5" r="0.5">
        <stop offset="0" stop-color="#4fb4ff" stop-opacity="0.85"/>
        <stop offset="0.5" stop-color="#1d6fd6" stop-opacity="0.55"/>
        <stop offset="1" stop-color="#0d2470" stop-opacity="0"/>
      </radialGradient>
    </defs>

    <rect class="paper-haze" x="500" y="0" width="700" height="320" fill="url(#haze)"/>

    <g role="img" aria-label="Glowing digital shield with a keyhole over a dark world map linked by network lines">
      <path class="image-band"
            d="M0 262 L820 262 C900 262 930 240 960 160 C990 70 1020 0 1090 0 L1200 0 L1200 560
               L450 560 C380 560 350 590 320 660 C290 740 270 801 210 801 L0 801 Z"
            fill="url(#bandFill)"/>
      <ellipse cx="960" cy="270" rx="250" ry="230" fill="url(#shieldGlow)"/>
    </g>

    <path class="accent-strip" d="M560 252 L830 252 C880 252 905 240 925 205 L935 212 C915 250 885 266 830 266 L550 266 Z" fill="var(--sky)"/>
    <path class="accent-strip" d="M420 585 L560 585 L548 600 L410 600 Z" fill="var(--sky)"/>
    <path class="accent-strip" d="M230 770 C270 770 290 745 310 700 L320 706 C300 752 282 784 236 784 Z" fill="var(--sky)"/>
  </svg>

  <header class="brand">
    <div class="brand-row">
      <span class="brand-mark"></span>
      <span class="brand-name">TOREVA</span>
    </div>
    <span class="brand-tagline">company tagline here</span>
  </header>

  <section class="headline">
    <h1>Capabilities Statement<br>of Cyber &amp; Information<br>Security</h1>
    <p class="intro">This is capabilities brief for a company<br>that does <span class="accent">cyber and information security</span></p>
  </section>

  <p class="website">www.torevacybersecurity.com</p>
</main>
</body>
</html>
```